Tree Service Billboard 20x8 ft

We need a billboard design for a tree service company.
The billboard is 20ft x 8 ft so we need a design that is capable to stretching to those dimensions without loosing quality.
I have attached a series of images.
Image 1- Simply a billboard that I think looks good that I would like you to use for inspiration. I am aiming for the same format only no color in the wording, just black white, or gray. I like the the trees in the background, the logo placed to the left, and wording on the right.
Image 2- Current Logo I would like to the left of the billboard
Image 3- Another format of current logo if needed.
Image 4- A drawn out design template
Image 5- Another drawn out design template

Specific things I am looking for
-The contact number to be the largest thing on the design
-The logo on the design
-Key points to the design to say:
Tree Removal
Tree Trimming
Land Development
Stump Grinding
Storm Response
Insured
Free Bids
-The facebook logo
-The Google Logo

```html
<!DOCTYPE html>
<html lang="en">
<head>
<meta charset="utf-8">
<title>Birch Hollow Tree Care – Billboard</title>
<link href="https://fonts.googleapis.com/css2?family=Bebas+Neue&family=Poppins:ital,wght@0,700;1,700&display=swap" rel="stylesheet">
<style>
  :root {
    --page: #ffffff;
    --ink: #0b0b0b;
    --white: #ffffff;
    --leaf-dark: #4f7d1c;
    --leaf-mid: #7fb327;
    --leaf-light: #b9d640;
    --sun: #e8e46a;
    --trunk: #5a5a2a;
  }
  * { margin: 0; padding: 0; box-sizing: border-box; }
  html, body {
    width: 1200px; height: 825px; overflow: hidden;
    background: var(--page);
  }
  .billboard {
    position: absolute; left: 20px; top: 182px;
    width: 1160px; height: 461px;
    overflow: hidden;
  }
  .scene {
    position: absolute; left: 0; top: 0; width: 1160px; height: 347px;
    background:
      radial-gradient(ellipse 380px 260px at 1120px 20px, rgba(240,235,120,.95), rgba(240,235,120,0) 70%),
      linear-gradient(90deg, var(--trunk) 0%, var(--leaf-dark) 8%, var(--leaf-mid) 35%, var(--leaf-mid) 65%, var(--leaf-light) 88%, var(--sun) 100%);
  }
  .scene::after {
    content: ""; position: absolute; left: 0; right: 0; bottom: 0; height: 110px;
    background: linear-gradient(180deg, rgba(150,200,40,0) 0%, rgba(160,205,45,.85) 100%);
  }
  .brand-ring {
    position: absolute; left: 287px; top: 33px;
    width: 178px; height: 178px; border-radius: 50%;
    border: 6px solid var(--white);
  }
  .brand-name {
    position: absolute; left: 179px; top: 218px; width: 404px;
    font-family: "Bebas Neue", sans-serif; font-size: 66px; line-height: 1;
    color: var(--white); text-align: center; white-space: nowrap;
  }
  .brand-phone {
    position: absolute; left: 179px; top: 283px; width: 404px;
    display: flex; align-items: center; gap: 12px;
    font-family: "Bebas Neue", sans-serif; font-size: 34px; line-height: 1;
    color: var(--white); letter-spacing: .04em;
  }
  .brand-phone::before, .brand-phone::after {
    content: ""; flex: 1; height: 3px; background: var(--white);
  }
  .services {
    position: absolute; left: 826px; top: 56px; width: 334px;
    list-style: none;
  }
  .services li {
    position: relative; height: 29px; margin-bottom: 8px;
    background: var(--white); border-radius: 15px 0 0 15px;
    padding-left: 46px;
    font-family: "Poppins", sans-serif; font-style: italic; font-weight: 700;
    font-size: 23px; line-height: 30px; color: var(--ink);
    text-transform: uppercase; white-space: nowrap; letter-spacing: -.01em;
  }
  .services .tick {
    position: absolute; left: 8px; top: 4px; width: 21px; height: 21px;
  }
  .contact-band {
    position: absolute; left: 0; top: 347px; width: 1160px; height: 114px;
    background: var(--ink);
  }
  .contact-band .phone-icon {
    position: absolute; left: 32px; top: 27px; width: 62px; height: 62px;
  }
  .contact-band .number {
    position: absolute; left: 130px; top: 8px;
    font-family: "Poppins", sans-serif; font-weight: 700; font-size: 86px;
    line-height: 100px; color: var(--white); letter-spacing: .13em;
    white-space: nowrap;
  }
  .social {
    position: absolute; top: 23px; width: 72px; height: 72px;
    border-radius: 50%; background: var(--white);
  }
  .social.first { left: 906px; }
  .social.second { left: 989px; }
</style>
</head>
<body>
  <main class="billboard">
    <div class="scene" role="img" aria-label="Sunlit park with large leafy trees over a green lawn"></div>

    <div class="brand-ring" aria-hidden="true"></div>
    <h1 class="brand-name">Birch Hollow Tree Care</h1>
    <p class="brand-phone">417-555-0148</p>

    <ul class="services">
      <li><svg class="tick" viewBox="0 0 20 20"><circle cx="10" cy="10" r="10" fill="#0b0b0b"/><path d="M5.5 10.3l3 3 6-6.3" fill="none" stroke="#fff" stroke-width="2.2" stroke-linecap="round" stroke-linejoin="round"/></svg>Tree Removal</li>
      <li><svg class="tick" viewBox="0 0 20 20"><circle cx="10" cy="10" r="10" fill="#0b0b0b"/><path d="M5.5 10.3l3 3 6-6.3" fill="none" stroke="#fff" stroke-width="2.2" stroke-linecap="round" stroke-linejoin="round"/></svg>Tree Trimming</li>
      <li><svg class="tick" viewBox="0 0 20 20"><circle cx="10" cy="10" r="10" fill="#0b0b0b"/><path d="M5.5 10.3l3 3 6-6.3" fill="none" stroke="#fff" stroke-width="2.2" stroke-linecap="round" stroke-linejoin="round"/></svg>Land Development</li>
      <li><svg class="tick" viewBox="0 0 20 20"><circle cx="10" cy="10" r="10" fill="#0b0b0b"/><path d="M5.5 10.3l3 3 6-6.3" fill="none" stroke="#fff" stroke-width="2.2" stroke-linecap="round" stroke-linejoin="round"/></svg>Stump Grinding</li>
      <li><svg class="tick" viewBox="0 0 20 20"><circle cx="10" cy="10" r="10" fill="#0b0b0b"/><path d="M5.5 10.3l3 3 6-6.3" fill="none" stroke="#fff" stroke-width="2.2" stroke-linecap="round" stroke-linejoin="round"/></svg>Storm Response</li>
      <li><svg class="tick" viewBox="0 0 20 20"><circle cx="10" cy="10" r="10" fill="#0b0b0b"/><path d="M5.5 10.3l3 3 6-6.3" fill="none" stroke="#fff" stroke-width="2.2" stroke-linecap="round" stroke-linejoin="round"/></svg>Insured</li>
      <li><svg class="tick" viewBox="0 0 20 20"><circle cx="10" cy="10" r="10" fill="#0b0b0b"/><path d="M5.5 10.3l3 3 6-6.3" fill="none" stroke="#fff" stroke-width="2.2" stroke-linecap="round" stroke-linejoin="round"/></svg>Free Bids</li>
    </ul>

    <section class="contact-band">
      <svg class="phone-icon" viewBox="0 0 64 64" aria-hidden="true">
        <path d="M14 6c3-2 6-1 8 2l6 9c1.5 2.5 1 5-1 7l-4 3c2 6 8 13 15 17l3-4c2-2 5-2.5 7-1l9 6c3 2 4 5 2 8l-4 5c-3 3-8 4-13 2C27 53 11 37 5 22 3 17 4 12 8 9z" fill="#fff"/>
        <path d="M38 14a14 14 0 0 1 12 12" fill="none" stroke="#fff" stroke-width="4" stroke-linecap="round"/>
        <path d="M40 4a24 24 0 0 1 20 20" fill="none" stroke="#fff" stroke-width="4" stroke-linecap="round"/>
      </svg>
      <p class="number">417.555.0148</p>
      <span class="social first" aria-hidden="true"></span>
      <span class="social second" aria-hidden="true"></span>
    </section>
  </main>
</body>
</html>
```